PerkHaven.com.au Web Redesign

We need a web redesign for our existing website at http://perkhaven.com.au. Our website hosts a registration form for users who are interested in surveys, samples/trials, competitions (contests), and freebie offers. We rely heavily on emails as our main tool to communicate with our users. The current theme of our website is really white and bright. We would like to see a rather bold but playful theme like red, orange, and dark grey. The final design should be able to: 1) entice users to register; 2) look fun & playful; 3) have the modern, but colorful touch; and 4) present the theme of the offers (i.e. Tarlo, Brisk/Pinemarket, and Harlow Vance gift cards). The current logo can be redesigned into a new logo to suit the new web design.
Updates

Your new design must cover the following pages:

/index.html
/catalogue.html
/confirm-your-subscription.html
/contact-us.html
/daily-deals.html
/faqs.html
/terms-of-use.html
/thank-you.html

I missed out two extra pages that should be included in this project

/restaurant.html
/travel.html

Project Deadline Extended
Reason: Deadline is now extended by 15 more days. This should give you more time to be creative.

Target Market(s)

Age 18-65, both males & females, any occupations.

Requirements
Must have
• The new design must have the corresponding theme of the offer presented (Tarlo, BRISK/Pinemarket, and Harlow Vance).
Nice to have
• The current layout of our website crams all 3 gift card offers into one page. Feel free to redesign the website into 3 different pages with each page containing a dedicated offer. This will enhance the theme of the offer presented.

```html
<!DOCTYPE html>
<html lang="en">
<head>
<meta charset="utf-8">
<title>PerkHaven – Frequently Asked Questions</title>
<link href="https://fonts.googleapis.com/css2?family=PT+Sans+Narrow:wght@700&family=PT+Sans:wght@400&display=swap" rel="stylesheet">
<style>
  :root {
    --ink: #222629;
    --text: #333;
    --muted: #555;
    --brand-red: #c9141b;
    --nav-active: #c8090f;
    --band-top: #4a5660;
    --band-bottom: #2a333a;
    --frame: #56626b;
    --rule: #d9d9d9;
    --footer-bg: #f4f4f4;
    --white: #ffffff;
  }
  * { box-sizing: border-box; margin: 0; padding: 0; }
  html, body { width: 715px; height: 1200px; overflow: hidden; background: var(--white); }
  body { position: relative; font-family: "PT Sans", Arial, sans-serif; color: var(--text); }

  .site-header { position: absolute; top: 0; left: 0; width: 715px; height: 72px; }
  .brand { position: absolute; left: 36px; top: 22px; }
  .brand-name { font-family: "PT Sans Narrow", Arial, sans-serif; font-weight: 700; font-size: 26px; color: var(--brand-red); line-height: 1; }
  .brand-tagline { font-size: 7.5px; letter-spacing: .3px; color: var(--muted); margin-top: 2px; }

  .main-nav { position: absolute; right: 32px; top: 37px; display: flex; align-items: center; font-family: "PT Sans Narrow", Arial, sans-serif; font-weight: 700; font-size: 12px; color: var(--ink); }
  .main-nav a { color: inherit; text-decoration: none; padding: 2px 9px; border-left: 1px solid #bbb; line-height: 11px; }
  .main-nav a:first-child { border-left: none; }
  .main-nav a.is-active { background: var(--nav-active); color: var(--white); border-left: none; padding: 4px 13px; border-radius: 2px; }
  .main-nav a.is-active + a { border-left: none; }

  .hero-band { position: absolute; top: 72px; left: 0; width: 715px; height: 248px; background: linear-gradient(var(--band-top), var(--band-bottom)); }
  .hero-frame { position: absolute; left: 27px; top: 8px; width: 661px; height: 234px; background: var(--frame); border-radius: 3px; }
  .hero-photo { position: absolute; left: 6px; top: 6px; width: 648px; height: 219px; border-radius: 2px; background: linear-gradient(90deg, #d9dde0 0%, #eef1f3 40%, #f6f8f9 75%, #e5eaee 100%); }

  .faq { position: absolute; top: 352px; left: 0; width: 715px; }
  .faq-title { position: absolute; left: 41px; top: 0; font-family: "PT Sans Narrow", Arial, sans-serif; font-weight: 700; font-size: 19px; color: var(--ink); }
  .faq-item { position: absolute; left: 41px; width: 633px; padding-bottom: 14px; border-bottom: 1px solid var(--rule); }
  .faq-item:last-child { border-bottom: none; }
  .faq-q { font-size: 10.5px; color: var(--ink); margin-bottom: 5px; }
  .faq-a { font-size: 8px; line-height: 14px; color: var(--text); }

  .site-footer { position: absolute; top: 1100px; left: 0; width: 715px; height: 100px; background: linear-gradient(var(--footer-bg), var(--white)); }
  .footer-nav { position: absolute; left: 38px; top: 23px; font-size: 8.5px; color: var(--ink); }
  .footer-nav a { color: inherit; text-decoration: none; }
  .footer-nav .sep { margin: 0 5px; }
  .copyright { position: absolute; left: 38px; top: 44px; font-size: 7.5px; color: var(--muted); }
  .social { position: absolute; right: 53px; top: 18px; display: flex; gap: 6px; }
</style>
</head>
<body>
  <header class="site-header">
    <div class="brand">
      <div class="brand-name">PerkHaven</div>
      <div class="brand-tagline">BRINGING AUSSIE'S BEST REWARDS TO YOU</div>
    </div>
    <nav class="main-nav">
      <a href="#">MAIN</a>
      <a href="#">COMPETITIONS</a>
      <a href="#">SURVEYS</a>
      <a href="#">FREEBIES</a>
      <a href="#" class="is-active">FAQ</a>
      <a href="#">ABOUT US</a>
      <a href="#">TERM OF USE</a>
    </nav>
  </header>

  <section class="hero-band">
    <div class="hero-frame">
      <div class="hero-photo" role="img" aria-label="Photo of a smiling group of young professionals seated in a row in a bright office"></div>
    </div>
  </section>

  <main class="faq">
    <h1 class="faq-title">Frequently Asked Questions</h1>

    <div class="faq-item" style="top:38px">
      <h2 class="faq-q">What is PerkHaven?</h2>
      <p class="faq-a">PerkHaven is website that delivers quality competitions, surveys, and freebies from trusted sources. All offers are 100% free and require no purchases or credit card. Our mission is to offer you rewarding online experience through free stuff.</p>
    </div>

    <div class="faq-item" style="top:116px">
      <h2 class="faq-q">Why should I sign up with PerkHaven?</h2>
      <p class="faq-a">By becoming a member at PerkHaven, you will have access to our weekly newsletter with an exclusive offer. This offer may not be available on our site, so don't miss out any winning opportunity. Plus, you will also be automatically included in our monthly prize draw.</p>
    </div>

    <div class="faq-item" style="top:197px">
      <h2 class="faq-q">Is my information safe from spammers?</h2>
      <p class="faq-a">DEFINITELY! We value your privacy and will never sell and share your information to third parties. We keep your information with the most advanced and secure technology to prevent any unauthorised access.</p>
    </div>

    <div class="faq-item" style="top:274px">
      <h2 class="faq-q">Why do I have to provide detailed information (e.g. income level, date of birth, etc) during registration process?</h2>
      <p class="faq-a">It is important if you can provide us with accurate information as we will be using it to deliver a more targeted offer to you based on your profile. However, this information is not compulsory during the sign-up process.</p>
    </div>

    <div class="faq-item" style="top:355px">
      <h2 class="faq-q">What will I get on my email if I sign up?</h2>
      <p class="faq-a">Members will have exclusive access to our new free offers and freebie of the week, which may not be available on our website. They can range from offer to enter competitions, completing surveys, or a simple sign up to get free stuff.</p>
    </div>

    <div class="faq-item" style="top:434px">
      <h2 class="faq-q">Are these offers free to join?</h2>
      <p class="faq-a">The decision is up to you as all of these offers are 100% free to enter. You will get nothing but the chance of winning the rewards and prizes by joining the competitions and surveys.</p>
    </div>

    <div class="faq-item" style="top:507px">
      <h2 class="faq-q">Do I get paid by filling online surveys?</h2>
      <p class="faq-a">We sometimes provide online surveys from companies that are willing to offer cash to survey participants. Make sure you keep an eye on this offer as it would mean a bonus offer for you.</p>
    </div>

    <div class="faq-item" style="top:581px">
      <h2 class="faq-q">Who can become a member at PerkHaven?</h2>
      <p class="faq-a">Ideally, you should be an Australian resident to join our membership. However, we do have some international freebies and competitions, so there is no reason for you not to join if you are from overseas.</p>
    </div>

    <div class="faq-item" style="top:663px">
      <h2 class="faq-q">Can I cancel my account with PerkHaven?</h2>
      <p class="faq-a">Yes, you just need to click on "Unsubscribe" link in our emails to you. Once you are unsubscribed, you will stop receiving our weekly email newsletter.</p>
    </div>
  </main>

  <footer class="site-footer">
    <nav class="footer-nav">
      <a href="#">PRIVACY POLICY</a><span class="sep">|</span><a href="#">FAQS</a><span class="sep">|</span><a href="#">ABOUT US</a><span class="sep">|</span><a href="#">CONTACT US</a><span class="sep">|</span><a href="#">TERMS OF USE</a>
    </nav>
    <p class="copyright">© 2013 Company Name.&nbsp; All right reserved.&nbsp; Term of Use</p>
    <div class="social" aria-label="Social links">
      <svg width="17" height="17" viewBox="0 0 17 17"><circle cx="8.5" cy="8.5" r="8" fill="#555"/></svg>
      <svg width="17" height="17" viewBox="0 0 17 17"><circle cx="8.5" cy="8.5" r="8" fill="#555"/></svg>
      <svg width="17" height="17" viewBox="0 0 17 17"><circle cx="8.5" cy="8.5" r="8" fill="#555"/></svg>
    </div>
  </footer>
</body>
</html>
```